Vordaline - Fitness Coach. Needs a Business Card Design that I can also use for other advertising

Established 2012, I have finished the KTRB National Certificate in Fitness & Personal Training. Harlow Cross First Aid Certificate. I have the Auckland 800m track records for MW45. I also came 1st at the 2012 Pellamar Games in 800 & 1500m. I am passionate about health & fitness and would like to help people reach their health & fitness goals. I also take health & fitness weekends. Main interests - Running, Weight Training, Yoga & Aqua Jogging. I like strength/power, but am femine.

Target Market(s)

Male or Female 18 and over that wants to improve their health & fitness

Industry/Entity Type

Advertising

Requirements
Must have
• my name: Rosalind K Tarbury contact details: ros@quillsend.co.nz mobile - 021 583917 URL name: facebook.com/rosalindKtarbury - VordaLine
Photo of Me

```html
<!DOCTYPE html>
<html lang="en">
<head>
<meta charset="utf-8">
<title>Rosalind K Tarbury — Business Card</title>
<link rel="stylesheet" href="https://fonts.googleapis.com/css2?family=Della+Respira&family=Tinos&display=swap">
<style>
  :root {
    --page-bg: #d8cdbf;
    --card-black: #050606;
    --ink-white: #ffffff;
    --foliage-dark: #1f3517;
    --foliage-mid: #3f6a2c;
    --accent-orange: #e8682a;
  }
  * { margin: 0; padding: 0; box-sizing: border-box; }
  html, body {
    width: 971px; height: 1200px; overflow: hidden;
    background: var(--page-bg);
  }
  .canvas { position: relative; width: 971px; height: 1200px; }
  .card {
    position: absolute; left: 86px; width: 799px; height: 456px;
    background: var(--card-black);
    border-radius: 22px; overflow: hidden;
    color: var(--ink-white);
  }
  .card--front { top: 89px; }
  .card--back { top: 655px; }

  .portrait-area {
    position: absolute; left: 0; top: 0; width: 330px; height: 100%;
    background:
      linear-gradient(90deg, rgba(5,6,6,0) 0%, rgba(5,6,6,0) 55%, var(--card-black) 100%),
      radial-gradient(ellipse at 40% 55%, var(--foliage-mid) 0%, var(--foliage-dark) 70%);
  }

  .contact-list {
    position: absolute; right: 44px; top: 30px;
    list-style: none; text-align: right;
    font-family: "Tinos", "Times New Roman", serif;
    font-size: 24px; line-height: 40px;
  }
  .contact-list li { display: flex; justify-content: flex-end; align-items: center; gap: 6px; }
  .contact-icon { width: 16px; height: 22px; }
  .contact-at { font-weight: bold; font-size: 20px; }
  .social-square { width: 10px; height: 18px; background: var(--ink-white); margin-right: 4px; }

  .brand-name, .brand-tagline { font-family: "Della Respira", Georgia, serif; white-space: nowrap; }
  .card--front .brand-block { position: absolute; left: 332px; top: 350px; }
  .card--front .brand-name { font-size: 33px; line-height: 44px; }
  .card--front .brand-tagline { font-size: 15px; line-height: 22px; }

  .card--back .brand-block {
    position: absolute; left: 0; right: 0; top: 138px; text-align: center;
  }
  .card--back .brand-name { font-size: 66px; line-height: 84px; }
  .card--back .brand-tagline { font-size: 31px; line-height: 56px; }
</style>
</head>
<body>
<main class="canvas">
  <section class="card card--front">
    <div class="portrait-area" role="img" aria-label="Photo of Rosalind jumping with a raised fist in an orange top, in front of green foliage"></div>
    <ul class="contact-list">
      <li>
        <svg class="contact-icon" viewBox="0 0 16 22" aria-hidden="true">
          <rect x="2" y="3" width="12" height="18" rx="2" fill="#fff"/>
          <rect x="4" y="0" width="2" height="4" fill="#fff"/>
          <rect x="4" y="6" width="8" height="5" fill="#050606"/>
          <rect x="4" y="13" width="2" height="2" fill="#050606"/><rect x="7" y="13" width="2" height="2" fill="#050606"/><rect x="10" y="13" width="2" height="2" fill="#050606"/>
          <rect x="4" y="16" width="2" height="2" fill="#050606"/><rect x="7" y="16" width="2" height="2" fill="#050606"/><rect x="10" y="16" width="2" height="2" fill="#050606"/>
        </svg>
        <span>021 583917</span>
      </li>
      <li><span class="contact-at">@</span><span>ros@quillsend.co.nz</span></li>
      <li><span class="social-square"></span><span>Vordaline</span></li>
    </ul>
    <div class="brand-block">
      <p class="brand-name">Rosalind K Tarbury</p>
      <p class="brand-tagline">meeting your health &amp; fitness goals</p>
    </div>
  </section>

  <section class="card card--back">
    <div class="brand-block">
      <p class="brand-name">Rosalind K Tarbury</p>
      <p class="brand-tagline">meeting your health &amp; fitness goals</p>
    </div>
  </section>
</main>
</body>
</html>
```